Founder / concept developer needs business card // Consultant needs VCARD

I need a business card for me as a founding consultant in Berlin. I advise entrepreneurs, especially in the design of business ideas, business plans or financing applications. More information about this in the annexes. My USP: I design / structure complex ideas and projects convincingly so that my client is successful. I want to communicate professionalism, effectiveness and clarity. Colors like from the range BLACK-GRAY-GREEN. I am 27 years old, I have studied business for 7 years. Attachments: - Business card design (only idea, do not focus on it) - Website screenshot (only idea, do not focus on it)

Target Market(s)

Target group: Founder (20-50 yrs, m / w, needy, in "break-up phase") and CONTRACTOR / "financier" (30-55 yrs, m / w, often public service "routine-oriented"). The foundations are in quite different industries: digital, craft, tourism, retail, services, etc. Almost all German.

Industry/Entity Type

Consultant

Contact Information for Business Card

Lukas Brenner
M. Sc., International Business Administration
Gründungsberater, Konzeptentwickler
www.falkor-plan.de
kontakt@falkor-plan.de
Tel. 0157 284 3361

Colors

Designer to choose colors to be used in the design.

Requirements
Must have
• Professionalism, persuasiveness, clarity
Nice to have
• memorability
Should not have
• Schnörkelei

```html
<!DOCTYPE html>
<html lang="de">
<head>
<meta charset="utf-8">
<title>Lukas Brenner – Visitenkarte</title>
<link rel="stylesheet" href="https://fonts.googleapis.com/css2?family=Montserrat:wght@400;500&family=Roboto:wght@400&display=swap">
<style>
  :root {
    --stage: #2a2a2c;
    --card-dark: #141414;
    --card-light: #f7f8f7;
    --green: #3aa53f;
    --ink: #1b1b1b;
    --ink-soft: #6b6b6b;
    --rule: #c9c9c9;
    --name-light: #d9d9d9;
    --photo-a: #d2d2d2;
    --photo-b: #8a8a8a;
  }
  * { box-sizing: border-box; margin: 0; padding: 0; }
  html, body { width: 1200px; height: 1200px; overflow: hidden; }
  body {
    background: var(--stage);
    font-family: "Roboto", Arial, sans-serif;
    position: relative;
  }
  .card {
    position: absolute;
    left: 150px;
    width: 900px;
    height: 515px;
    overflow: hidden;
    box-shadow: 0 10px 30px rgba(0,0,0,.45);
  }
  /* front */
  .card--front { top: 60px; background: var(--card-dark); }
  .brand {
    position: absolute;
    top: 120px; left: 0; right: 0;
    text-align: center;
  }
  .brand__square {
    display: block;
    width: 160px; height: 110px;
    margin: 0 auto 26px;
    border: 4px solid var(--green);
  }
  .brand__name {
    font-family: "Montserrat", Arial, sans-serif;
    font-weight: 500;
    font-size: 30px;
    letter-spacing: 4px;
    color: var(--name-light);
  }
  .brand__url {
    margin-top: 6px;
    font-family: "Montserrat", Arial, sans-serif;
    font-size: 17px;
    letter-spacing: 1.5px;
    color: var(--green);
  }
  /* back */
  .card--back { top: 625px; background: var(--card-light); }
  .contact {
    position: absolute;
    left: 40px; top: 270px;
  }
  .contact__tel {
    font-family: "Montserrat", Arial, sans-serif;
    font-size: 26px;
    color: var(--ink);
    letter-spacing: 1px;
  }
  .contact__rule {
    position: absolute;
    left: 40px; top: 312px;
    width: 460px; height: 1px;
    background: var(--rule);
  }
  .contact__list {
    list-style: none;
    margin-top: 14px;
  }
  .contact__item {
    display: flex; align-items: center; gap: 8px;
    font-size: 20px;
    color: var(--ink-soft);
    line-height: 30px;
  }
  .contact__item svg { width: 22px; height: 18px; flex: none; }
  .contact__sep { color: var(--rule); }
  .profile {
    position: absolute;
    right: 50px; top: 150px;
    text-align: right;
  }
  .profile__photo {
    width: 330px; height: 200px;
    margin-left: auto;
    background: linear-gradient(160deg, var(--photo-a), var(--photo-b));
  }
  .profile__name {
    margin-top: 6px;
    margin-left: auto;
    width: 330px;
    font-family: "Montserrat", Arial, sans-serif;
    font-weight: 500;
    font-size: 28px;
    letter-spacing: 3px;
    color: var(--ink);
    padding-bottom: 6px;
    border-bottom: 1px solid var(--rule);
    white-space: nowrap;
  }
  .profile__title {
    margin-top: 8px;
    font-size: 20px;
    line-height: 30px;
    color: var(--ink-soft);
    white-space: nowrap;
  }
  .profile__title span { display: block; }
</style>
</head>
<body>
  <section class="card card--front">
    <div class="brand">
      <span class="brand__square"></span>
      <p class="brand__name">LUKAS BRENNER</p>
      <p class="brand__url">www.falkor-plan.de</p>
    </div>
  </section>

  <section class="card card--back">
    <div class="contact__rule"></div>
    <div class="contact">
      <p class="contact__tel">Tel. 0157 284 3361</p>
      <ul class="contact__list">
        <li class="contact__item">
          <svg viewBox="0 0 22 16" aria-hidden="true"><rect x="1" y="1" width="20" height="14" fill="var(--green)"/><path d="M1 1 L11 9 L21 1" fill="none" stroke="#fff" stroke-width="1.5"/></svg>
          <span class="contact__sep">|</span> kontakt@falkor-plan.de
        </li>
        <li class="contact__item">
          <svg viewBox="0 0 18 18" aria-hidden="true"><circle cx="9" cy="9" r="8" fill="var(--green)"/><path d="M1 9h16M9 1c-4 4-4 12 0 16M9 1c4 4 4 12 0 16" fill="none" stroke="#fff" stroke-width="1.2"/></svg>
          <span class="contact__sep">|</span> www.falkor-plan.de
        </li>
      </ul>
    </div>
    <div class="profile">
      <div class="profile__photo" role="img" aria-label="Schwarz-weißes Porträtfoto von Lukas Brenner"></div>
      <p class="profile__name">LUKAS BRENNER</p>
      <p class="profile__title">
        <span>M. Sc., International Business Administration</span>
        <span>Gründungsberater, Konzeptentwickler</span>
      </p>
    </div>
  </section>
</body>
</html>
```